Beacon Lending. We focus on mentoring our clients into a home. Partner Beacon Realty Group

Needing a Mortgage Company Website. We would like a mortgage calculator on the site as well as it linked to our partner sites.

We have 6 Other Websites that go into this.

We focus on helping our clients get approved for a home. We would like a mortgage calculator on it.
See other sites
www.harborvalehomes.example
www.keystepready.example

Target Market(s)

Modern, Average guy.

Industry/Entity Type

Mortgage Brokerage

Number of Pages Required

4 page

Font styles to use
Serif
Sans Serif

Colors
000000
0255a3
33a6d7

Requirements
Must have
• Plugins, Calculator, nice design, Contact form, SEO capability, etc.
Nice to have
• Someone I can hire for our 547 other sites. Finding a good designer is difficult and we have about 3 years worth of work.
Should not have
• You can pick the colors. Just Had some ideas. Please feel free to adjust it to your liking, You are the pro..
• We just want a nice clean friendly site we can capture leads on. We want to link our other companies and also Provide them worth Education and Tools to get approved for loan

```html
<!DOCTYPE html>
<html lang="en">
<head>
<meta charset="utf-8">
<title>Beacon Lending – Mortgage Brokerage</title>
<link href="https://fonts.googleapis.com/css2?family=Montserrat:wght@300;400;500;600;700&display=swap" rel="stylesheet">
<style>
:root{
  --blue:#33a6d7;
  --navy:#0255a3;
  --ink:#1d1f24;
  --text:#555b63;
  --muted:#8a9098;
  --panel:#eef1f4;
  --field:#e9ecef;
  --white:#ffffff;
  --red:#e84a5f;
  --gold:#ffd83a;
  --footer:#2c2f35;
}
*{box-sizing:border-box;margin:0;padding:0}
html,body{width:1200px;height:3586px;overflow:hidden}
body{font-family:'Montserrat',sans-serif;color:var(--ink);background:var(--white);position:relative}
.section{position:absolute;left:0;width:1200px}
.btn{display:inline-block;border:2px solid var(--blue);color:var(--ink);font-size:13px;font-weight:600;text-align:center;background:var(--white)}
.btn--solid{background:var(--blue);color:var(--white)}
.btn--ghost{background:transparent;color:var(--white)}

/* hero */
.hero{top:0;height:598px;background:linear-gradient(100deg,#3b3f44 0%,#6d6f70 35%,#a99d8a 60%,#4d5a6a 100%)}
.hero-photo{position:absolute;inset:0}
.hero-shade{position:absolute;inset:0;background:linear-gradient(90deg,rgba(20,25,30,.55),rgba(20,25,30,.1))}
.brand{position:absolute;left:98px;top:40px;color:var(--blue);font-size:22px;font-weight:500;letter-spacing:3px}
.nav{position:absolute;left:514px;top:46px;display:flex;gap:34px;font-size:13px;color:var(--white)}
.nav a{color:var(--white);text-decoration:none}
.nav a.active{color:var(--blue)}
.hero-phone{position:absolute;left:856px;top:43px;color:var(--white);font-size:16px;font-weight:600}
.hero-phone span{color:var(--blue)}
.hero-copy{position:absolute;left:200px;top:210px;color:var(--white)}
.hero-copy h1{font-size:52px;font-weight:300;line-height:1}
.hero-copy h2{font-size:25px;font-weight:600;margin-top:10px}
.hero-copy p{font-size:16px;line-height:1.5;width:250px;margin-top:12px}
.hero-copy .btn{margin-top:28px;width:162px;height:40px;line-height:36px}

/* differ */
.differ{top:598px;height:585px;text-align:center}
.section-title{font-size:25px;font-weight:500;line-height:1.4;color:var(--ink)}
.differ .section-title{position:absolute;top:60px;left:0;width:1200px}
.cards{position:absolute;top:157px;left:200px;display:flex;gap:40px}
.card{width:240px}
.card-photo{width:240px;height:158px}
.card h3{color:var(--blue);font-size:14px;font-weight:600;line-height:1.45;margin-top:22px}
.card p{color:var(--text);font-size:11.5px;line-height:1.7;margin-top:4px}
.differ .btn{position:absolute;top:480px;left:536px;width:128px;height:34px;line-height:30px;font-size:12px}

/* denied */
.denied{top:1183px;height:383px;background:var(--panel)}
.denied-photo{position:absolute;left:0;top:0;width:600px;height:383px;background:linear-gradient(160deg,#9fb4c8 0%,#6b5a48 45%,#3e3226 80%,#5f6b55 100%)}
.denied-copy{position:absolute;left:700px;top:55px;width:320px}
.denied-copy h2{font-size:24px;font-weight:500;line-height:1.35}
.denied-copy p{font-size:12px;color:var(--text);line-height:1.6;margin-top:14px}
.denied-copy p strong{color:var(--blue);font-weight:600}
.denied-copy .btn{margin-top:26px;width:128px;height:34px;line-height:30px;font-size:12px}

/* calculator */
.calc{top:1566px;height:449px}
.calc .section-title{position:absolute;top:60px;left:0;width:1200px;text-align:center}
.calc-label{position:absolute;left:200px;top:192px;color:var(--blue);font-size:13px;font-weight:500}
.calc-rule{position:absolute;left:200px;top:218px;width:500px;height:1px;background:var(--field)}
.calc-fields{position:absolute;left:200px;top:240px;display:grid;grid-template-columns:240px 240px;gap:18px 20px}
.field{height:34px;background:var(--field);font-size:9px;color:var(--muted);letter-spacing:1px;padding:0 14px;display:flex;align-items:center;justify-content:space-between}
.field svg{width:9px;height:6px}
.calc .btn{position:absolute;left:200px;top:341px;width:160px;height:32px;line-height:28px;font-size:12px}
.calc-divider{position:absolute;left:726px;top:140px}
.result{position:absolute;left:797px;top:190px;width:200px;height:200px;border-radius:50%;background:var(--red);color:var(--white);text-align:center;box-shadow:0 10px 30px rgba(232,74,95,.3)}
.result-label{font-size:14px;margin-top:38px;color:#3a1015}
.result-line{width:140px;height:1px;background:rgba(255,255,255,.4);margin:8px auto 0}
.result-value{font-size:38px;font-weight:600;color:var(--gold);margin-top:14px}
.result-value sup{font-size:15px}
.result-note{font-size:10px;margin-top:4px}

/* advantage */
.advantage{top:2015px;height:383px;background:linear-gradient(110deg,#4a4843 0%,#8e8a82 40%,#b7b2a8 60%,#5e5a52 100%)}
.advantage-shade{position:absolute;inset:0;background:rgba(25,28,32,.35)}
.advantage h2{position:absolute;top:140px;left:220px;width:760px;text-align:center;color:var(--white);font-size:23px;font-weight:600;line-height:1.35}
.stats{top:2398px;height:191px;background:var(--panel)}
.stat{position:absolute;top:-60px;width:200px;text-align:center;font-size:13px;font-weight:500;line-height:1.5;color:var(--ink)}
.stat-icon{width:120px;height:120px;margin:0 auto 14px;border-radius:50%;background:var(--white);display:flex;align-items:center;justify-content:center;box-shadow:0 6px 20px rgba(0,0,0,.08)}
.stat-icon.is-active{background:var(--blue)}
.stat-icon svg{width:44px;height:44px}

/* contact */
.contact{top:2589px;height:531px}
.contact-copy{position:absolute;left:200px;top:120px;width:400px}
.contact-copy h2{font-size:24px;font-weight:500;line-height:1.4}
.contact-copy p{font-size:12px;color:var(--text);line-height:1.7;margin-top:18px}
.contact-copy hr{border:0;height:1px;background:var(--field);margin:20px 0 22px}
.contact-phone{font-size:13px;color:var(--ink)}
.contact-phone span{color:var(--blue);font-weight:600}
.contact-email{font-size:12px;color:var(--text);margin-top:6px}
.contact-copy .btn{margin-top:20px;width:128px;height:34px;line-height:30px;font-size:12px}
.form-card{position:absolute;left:700px;top:64px;width:300px;height:447px;background:var(--white);box-shadow:0 10px 40px rgba(0,0,0,.1)}
.form-head{height:86px;background:var(--blue);color:var(--white);text-align:center;font-size:15px;font-weight:600;line-height:1.35;padding-top:16px;position:relative}
.form-head::after{content:"";position:absolute;left:140px;bottom:-10px;border:10px solid transparent;border-bottom:0;border-top-color:var(--blue)}
.form-body{padding:26px 25px 0}
.form-field{height:32px;background:var(--field);font-size:10px;color:var(--muted);padding:10px 14px;margin-bottom:12px}
.form-field.is-message{height:96px}
.send{position:absolute;left:126px;top:364px;width:48px;height:48px;border-radius:50%;background:var(--blue);display:flex;align-items:center;justify-content:center}

/* cta */
.cta{top:3120px;height:387px;background:linear-gradient(180deg,#1b2633 0%,#22303d 55%,#3b2f22 80%,#1c1a17 100%)}
.cta h2{position:absolute;top:145px;left:0;width:1200px;text-align:center;color:rgba(255,255,255,.92);font-size:46px;font-weight:300;line-height:1.3}

/* footer */
.footer{top:3507px;height:79px;background:var(--footer);color:#a8adb5;font-size:10px}
.footer-legal{position:absolute;left:200px;top:34px;display:flex;gap:18px}
.social{position:absolute;left:850px;top:24px;display:flex;gap:14px}
.social span{width:30px;height:30px;border-radius:50%;background:#4a4e55}
.to-top{position:absolute;left:1140px;top:30px}
</style>
</head>
<body>

<header class="section hero">
  <div class="hero-photo" role="img" aria-label="Photo of a smiling couple and an agent holding a tablet in front of a house"></div>
  <div class="hero-shade"></div>
  <div class="brand">Beacon Lending</div>
  <nav class="nav"><a class="active" href="#">Home</a><a href="#">About</a><a href="#">Our Process</a><a href="#">Contact</a></nav>
  <div class="hero-phone">Call Us Today! <span>(555) 014 – 2278</span></div>
  <div class="hero-copy">
    <h1>Big Dreams.</h1>
    <h2>Even bigger and better loans</h2>
    <p>An Intelligent way to make your dream come true!</p>
    <a class="btn btn--ghost">Get Loan Today!</a>
  </div>
</header>

<section class="section differ">
  <h2 class="section-title">How we differ when you<br>buying a home?</h2>
  <div class="cards">
    <div class="card">
      <div class="card-photo" role="img" aria-label="Photo of clients sitting with an advisor at a desk" style="background:linear-gradient(135deg,#e9eef2,#b7c4cf 60%,#6f8294)"></div>
      <h3>Sit with us before you with<br>a lender.</h3>
      <p>They will do a hard inquiry on your credit report and thus bring down your credit score just to tell you NO!</p>
    </div>
    <div class="card">
      <div class="card-photo" role="img" aria-label="Photo of business people shaking hands in an office" style="background:linear-gradient(135deg,#3d5a80,#8ea3bd 55%,#2c3a4f)"></div>
      <h3>We work with all lenders and all<br>brokers so we aren't biased.</h3>
      <p>We utilize all of them so we can have access to all of the home programs available not just a few.</p>
    </div>
    <div class="card">
      <div class="card-photo" role="img" aria-label="Photo of consultants reviewing paperwork together" style="background:linear-gradient(135deg,#c9d5de,#7f93a6 55%,#34414f)"></div>
      <h3>Get you approved today!</h3>
      <p>while work with our consultants and our agents.</p>
    </div>
  </div>
  <a class="btn">Consult Now!</a>
</section>

<section class="section denied">
  <div class="denied-photo" role="img" aria-label="Photo of a timber house with stone steps at sunset"></div>
  <div class="denied-copy">
    <h2>Are you trying to buy a home by siting with a lender or broker and get denied?</h2>
    <p>We understand your pain. They just <strong>pulled a hard inquiry on your credit profile</strong> just to damage in further.</p>
    <a class="btn btn--solid">Contact Us</a>
  </div>
</section>

<section class="section calc">
  <h2 class="section-title">Wouldn't you like to know if you can get<br>approved before you damage<br>your credit anymore?</h2>
  <div class="calc-label">Enter your Mortgage information</div>
  <div class="calc-rule"></div>
  <div class="calc-fields">
    <div class="field">LOAN AMOUNT<svg viewBox="0 0 9 6"><path d="M1 1l3.5 3.5L8 1" fill="none" stroke="#8a9098" stroke-width="1.3"/></svg></div>
    <div class="field">DEPOSIT<svg viewBox="0 0 9 6"><path d="M1 1l3.5 3.5L8 1" fill="none" stroke="#8a9098" stroke-width="1.3"/></svg></div>
    <div class="field">INTEREST RATE<svg viewBox="0 0 9 6"><path d="M1 1l3.5 3.5L8 1" fill="none" stroke="#8a9098" stroke-width="1.3"/></svg></div>
    <div class="field">PAYMENT TERM<svg viewBox="0 0 9 6"><path d="M1 1l3.5 3.5L8 1" fill="none" stroke="#8a9098" stroke-width="1.3"/></svg></div>
  </div>
  <a class="btn btn--solid">Calculate Now!</a>
  <svg class="calc-divider" width="44" height="300" viewBox="0 0 44 300"><path d="M2 0L40 150L2 300" fill="none" stroke="#e6e9ec" stroke-width="2"/></svg>
  <div class="result">
    <div class="result-label">Payment</div>
    <div class="result-line"></div>
    <div class="result-value">$25,603<sup>38</sup></div>
    <div class="result-note">In Total $350</div>
  </div>
</section>

<section class="section advantage">
  <div role="img" aria-label="Photo of agents and clients meeting and shaking hands" style="position:absolute;inset:0"></div>
  <div class="advantage-shade"></div>
  <h2>We also have an advantage! We work with every different lender/broker so we can offer you every program out there. Not just ones that are partners or let say "prefered vendors"</h2>
</section>

<section class="section stats">
  <div class="stat" style="left:201px">
    <div class="stat-icon is-active"><svg viewBox="0 0 44 44"><path d="M6 21L22 7l16 14M11 17v20h22V17M18 37V27h8v10" fill="none" stroke="#fff" stroke-width="2.4" stroke-linejoin="round"/></svg></div>
    Specialized Mortgage<br>Loan
  </div>
  <div class="stat" style="left:400px">
    <div class="stat-icon"><svg viewBox="0 0 44 44"><path d="M8 20h7v17H8zM15 21l7-12c3 0 4 2 3.5 5L24 19h10c2 0 3.5 2 3 4l-3 11c-.5 2-2 3-4 3H15" fill="none" stroke="#33a6d7" stroke-width="2.4" stroke-linejoin="round"/></svg></div>
    Stable Working<br>20+ Years
  </div>
  <div class="stat" style="left:600px">
    <div class="stat-icon"><svg viewBox="0 0 44 44"><path d="M29 13c-2-2-4-3-7-3-4 0-7 2-7 5.5 0 8 14 4.5 14 12.5 0 3.5-3 5.5-7 5.5-3 0-6-1-8-3.5M22 5v34" fill="none" stroke="#33a6d7" stroke-width="2.4" stroke-linecap="round"/></svg></div>
    More than 35,000<br>Loans
  </div>
  <div class="stat" style="left:799px">
    <div class="stat-icon"><svg viewBox="0 0 44 44"><path d="M13 7h18v10c0 6-4 10-9 10s-9-4-9-10zM13 11H7c0 6 3 9 7 9M31 11h6c0 6-3 9-7 9M22 27v7M15 38h14v-4H15z" fill="none" stroke="#33a6d7" stroke-width="2.4" stroke-linejoin="round"/></svg></div>
    Top -15 Ranking in<br>Mortgage
  </div>
</section>

<section class="section contact">
  <div class="contact-copy">
    <h2>Call Beacon Lending today and talk to one of our agents,</h2>
    <p>We can do a full financial analysis, pull your credit file, and figure out your DTI before you speak with a lender or broker.</p>
    <hr>
    <div class="contact-phone">Call Us Today! <span>(555) 014 – 2278</span></div>
    <div class="contact-email">e. info@harborvalehomes.example</div>
    <a class="btn">Contact Us</a>
  </div>
  <form class="form-card">
    <div class="form-head">Book your<br>Free Consultation!</div>
    <div class="form-body">
      <div class="form-field">Enter your Name</div>
      <div class="form-field">Email</div>
      <div class="form-field">Phone</div>
      <div class="form-field is-message">Message ...</div>
    </div>
    <div class="send"><svg width="20" height="18" viewBox="0 0 20 18"><path d="M1 1l18 8-18 8 3-8z" fill="#fff"/></svg></div>
  </form>
</section>

<section class="section cta">
  <div role="img" aria-label="Photo of a lit cabin among pine trees under a night sky" style="position:absolute;inset:0"></div>
  <h2>Ready to Buy your<br>Dream Home?</h2>
</section>

<footer class="section footer">
  <div class="footer-legal"><span>© 2018 Beacon Realty Group. All Rights Reserved.</span><span>|</span><span>Privacy policy</span><span>|</span><span>Terms &amp; Conditions</span></div>
  <div class="social"><span></span><span></span><span></span><span></span></div>
  <svg class="to-top" width="16" height="12" viewBox="0 0 16 12"><path d="M2 10l6-7 6 7" fill="none" stroke="#a8adb5" stroke-width="2"/></svg>
</footer>

</body>
</html>
```